Zielgruppe
Wir Produzieren ein Schauspiel mit dem Multitalent Mira Dellwig (bekannt vor allem durch ihren Auftritt beim „Nordlicht Liederpreis“) und der Schauspieler Bertl Wendl (bekannt z.B. aus den TV-Produktionen „Tannenhofsagen“ und „Der Zauber vom Kastanienweg“) sind die ideale Besetzung für den deutschsprachigen Raum. Eine Liebesgeschichte mit allen Höhen und Tiefen!
Zielgruppe 40+ und Frauen
Es ist Lustig!
Brauchen tolles, modernes Theaterplakat.
Aufgabenstellung
Tittel: Tango Tränen und Tapeten.
Format A0 und unten soll ein freier Balken für den Termin/Orts etc. Eindruck sein.
Ein Schauspiel, Komödie, soll Tickets verkaufen.
Kurze Beschreibung:
Ja, es wird eine Komödie, in der wir ein alterndes Ehepaar erleben, das beschlossen hat, sich zu trennen. Sie hat ihm gestanden, vor Kurzem eine Affäre gehabt zu haben, mit einem alten Freund, der eigentlich jetzt woanders wohnt, den sie aber vor Kurzem getroffen habe, woraufhin es (angeblich) zum mehrfachen Vollzug gekommen sei.
Das Stück beginnt am Morgen nach der Beichte und der Trennungsentscheidung, mit den beiden am Tisch und einer Kiste alter Briefe vor sich. Es sind all die Briefe, die sie sich über die Jahrzehnte geschrieben haben. Sie will seine Briefe zurückgeben, sie will ihre Briefe zurück etc. Sie sind übernächtigt, aufgewühlt, verheult, böse, usw.
Und dabei lesen sie sich gegenseitig die Briefe vor, kommentieren sie zynisch, tauchen aber in ihre Erinnerungen ein und durchleben nochmal ihr ganzes Eheleben. Das Ganze hatte begonnen, mit einer verbotenen Lehrer-Schülerin-Liebe mit viel Romantik, Geheimnistuerei, mit heimlichen Treffs, Gewissensbissen und Leidenschaften. Anhand der Briefe bekommen wir ihre ganze Geschichte präsentiert.
Sie haben auch einen Sohn, der woanders lebt, verheiratet ist, aber scheinbar keine Kinder kriegen kann.
Zur Mitte des Stückes machen die beiden sich bereit, zu einem Schuljahrgangstreffen. Beide gehen hin, aber getrennt.
Der zweite Akt beginnt mit ihm am Tisch, der kaum geschlafen hat, weil sie die ganze Nacht nicht zurückgekommen ist. Er hat sich Sorgen gemacht, bis sie morgens um 5 heroingetorkelt kam.
Sie fragen sich aus, sie werden eifersüchtig. Sie macht ihm Vorwürfe, er macht ihr Vorwürfe und plötzlich kommen sie endlich zu einer großen Aussprache über all das, was sie sich nie gesagt haben, was sie schon immer anders haben wollten, etc. ..

```html
<!DOCTYPE html>
<html lang="de">
<head>
<meta charset="utf-8">
<title>Tango, Tränen &amp; Tapeten – Theaterplakat</title>
<link rel="stylesheet" href="https://fonts.googleapis.com/css2?family=Amatic+SC:wght@400;700&display=swap">
<style>
  :root {
    --indigo: #332b82;
    --orange: #da7928;
    --orange-deep: #c9651f;
    --night: #212444;
    --white: #ffffff;
  }
  * { margin: 0; padding: 0; box-sizing: border-box; }
  html, body { width: 851px; height: 1200px; overflow: hidden; background: var(--indigo); }
  .poster {
    position: relative;
    width: 851px;
    height: 1200px;
    background: var(--indigo);
    font-family: "Amatic SC", "Arial Narrow", sans-serif;
    color: var(--white);
    text-transform: uppercase;
    overflow: hidden;
  }
  .heart-artwork { position: absolute; left: 48px; top: 165px; width: 803px; height: 890px; }
  .title { position: absolute; line-height: 0.85; font-weight: 700; }
  .title-line { display: block; }
  .title-tango { position: absolute; left: 98px; top: 62px; font-size: 150px; transform: rotate(-5deg); transform-origin: left bottom; }
  .title-traenen { position: absolute; left: 82px; top: 196px; font-size: 150px; transform: rotate(-3deg); transform-origin: left bottom; }
  .title-amp { position: absolute; left: 332px; top: 300px; font-size: 60px; }
  .title-tapeten { position: absolute; left: 165px; top: 340px; font-size: 160px; letter-spacing: 2px; }

  .tagline { position: absolute; font-weight: 700; line-height: 1; }
  .tag-eine { left: 287px; top: 535px; font-size: 22px; }
  .tag-liebes { left: 303px; top: 552px; font-size: 56px; }
  .tag-geschichte { left: 350px; top: 596px; font-size: 56px; }
  .tag-mit { left: 327px; top: 648px; font-size: 22px; }
  .tag-allen { left: 303px; top: 676px; font-size: 24px; transform: rotate(-8deg); }
  .tag-hoehen { left: 370px; top: 640px; font-size: 60px; }
  .tag-und { left: 535px; top: 662px; font-size: 24px; }
  .tag-tiefen { left: 440px; top: 690px; font-size: 60px; transform: rotate(-3deg); }
  .tag-bang { left: 602px; top: 660px; font-size: 68px; }

  .cast-intro { position: absolute; left: 236px; top: 780px; font-size: 20px; font-weight: 700; transform: rotate(-6deg); }
  .cast-name { position: absolute; font-weight: 700; line-height: 1; font-size: 40px; }
  .cast-mira { left: 268px; top: 796px; transform: rotate(-3deg); }
  .cast-amp { position: absolute; left: 478px; top: 804px; font-size: 16px; }
  .cast-bertl { left: 512px; top: 786px; transform: rotate(2deg); }
  .cast-note { position: absolute; font-size: 18px; font-weight: 700; line-height: 1.15; text-align: center; }
  .note-mira { left: 296px; top: 832px; width: 170px; transform: rotate(-4deg); }
  .note-bertl { left: 515px; top: 828px; width: 210px; transform: rotate(2deg); }

  .event-slot { position: absolute; left: 30px; top: 1030px; width: 789px; height: 140px; background: var(--white); }
</style>
</head>
<body>
<main class="poster">
  <svg class="heart-artwork" role="img" aria-label="Illustration: großes orangefarbenes Herz, von einem dunklen Blitz in zwei Hälften gespalten" viewBox="0 0 803 890">
    <defs>
      <linearGradient id="heartTone" x1="0" y1="0" x2="1" y2="1">
        <stop offset="0" stop-color="var(--orange)"/>
        <stop offset="1" stop-color="var(--orange-deep)"/>
      </linearGradient>
    </defs>
    <rect x="0" y="0" width="803" height="890" rx="60" fill="url(#heartTone)"/>
  </svg>

  <h1 class="title">
    <span class="title-line title-tango">Tango,</span>
    <span class="title-line title-traenen">Tränen</span>
    <span class="title-line title-amp">&amp;</span>
    <span class="title-line title-tapeten">Tapeten</span>
  </h1>

  <p class="tagline-group">
    <span class="tagline tag-eine">Eine</span>
    <span class="tagline tag-liebes">Liebes</span>
    <span class="tagline tag-geschichte">Geschichte</span>
    <span class="tagline tag-mit">mit</span>
    <span class="tagline tag-allen">allen</span>
    <span class="tagline tag-hoehen">Höhen</span>
    <span class="tagline tag-und">und</span>
    <span class="tagline tag-tiefen">Tiefen</span>
    <span class="tagline tag-bang">!</span>
  </p>

  <section class="cast">
    <p class="cast-intro">Gespielt von</p>
    <p class="cast-name cast-mira">Mira Dellwig</p>
    <span class="cast-amp">&amp;</span>
    <p class="cast-name cast-bertl">Bertl Wendl</p>
    <p class="cast-note note-mira">Bekannt durch<br>ihren Auftritt<br>beim „Nordlicht<br>Liederpreis“</p>
    <p class="cast-note note-bertl">Bekannt z.B. aus den<br>TV-Produktionen<br>„Tannenhofsagen“<br>und „Der Zauber vom<br>Kastanienweg“</p>
  </section>

  <div class="event-slot" aria-label="Freifläche für Termin und Ort"></div>
</main>
</body>
</html>
```